Financial Planning business needs a new Business Card design

We need a business card design for an Australian financial planning business. I am looking for a clean simple design

Target Market(s)

People aged 25-40

Industry/Entity Type

Financial Service

Contact Information for Business Card

On the front of the card we need the following information:
Name: Colin Merrow (First Name Green: #006838 and last name Grey: #414042)
Position: Financial Adviser
Qualifications: BEc(Hons), AdDipFS(FP), Dip FMBM, CFL®
Mobile: 0437 512 604
Email: colin@brightledgeplan.com.au

On the back of the card we need:
Postal address: PO BOX 5307, PERTH BC, WA 6849
Website: www.brightledgeplan.com.au
Text: AFS Licence No. 518760

The fields need to be able to be edited.

Font styles to use
Sans Serif

Requirements
Must have
• Information listed above

```html
<!DOCTYPE html>
<html lang="en">
<head>
<meta charset="UTF-8">
<title>Brightledge Business Card</title>
<link rel="stylesheet" href="https://fonts.googleapis.com/css2?family=Open+Sans:wght@400;600;700&display=swap">
<style>
  :root {
    --brand-green: #006838;
    --brand-grey: #414042;
    --text-dark: #333335;
    --card-white: #ffffff;
    --backdrop: #6b4a33;
  }
  * { margin: 0; padding: 0; box-sizing: border-box; }
  html, body { width: 1200px; height: 1000px; overflow: hidden; }
  body {
    background: var(--backdrop);
    font-family: "Open Sans", sans-serif;
    color: var(--text-dark);
    position: relative;
  }
  .card {
    position: absolute;
    left: 265px;
    width: 666px;
    height: 397px;
    background: var(--card-white);
    box-shadow: 0 4px 10px rgba(0,0,0,0.35);
  }
  .card--front { top: 73px; }
  .card--back { top: 532px; }

  .accent-bar {
    position: absolute;
    left: 0; top: 74px;
    width: 11px; height: 58px;
    background: var(--brand-green);
  }
  .wordmark {
    position: absolute;
    font-weight: 700;
    color: var(--brand-green);
    letter-spacing: 0.5px;
    line-height: 1;
  }
  .card--front .wordmark { left: 33px; top: 84px; font-size: 40px; }
  .card--back .wordmark { left: 45px; top: 159px; font-size: 40px; }

  .details {
    position: absolute;
    border-left: 2px solid var(--brand-grey);
  }
  .card--front .details {
    left: 370px; top: 224px;
    height: 140px;
    padding-left: 26px;
  }
  .person-name {
    font-size: 24px;
    font-weight: 600;
    line-height: 1;
    margin-top: -2px;
    text-transform: uppercase;
    color: var(--brand-grey);
  }
  .person-name .first { color: var(--brand-green); }
  .person-role, .person-quals {
    font-size: 16px;
    line-height: 22px;
    color: var(--brand-grey);
  }
  .person-role { margin-top: 4px; }
  .person-quals { margin-top: 4px; }
  .contact-list { list-style: none; margin-top: 10px; }
  .contact-list li {
    display: flex;
    align-items: center;
    gap: 8px;
    font-size: 16px;
    line-height: 24px;
    color: var(--brand-grey);
  }
  .contact-list svg { width: 15px; height: 12px; flex: none; }

  .card--back .details {
    left: 355px; top: 171px;
    height: 58px;
    padding-left: 14px;
  }
  .company-info {
    list-style: none;
    font-size: 15.5px;
    line-height: 22px;
    color: var(--brand-grey);
    margin-top: -5px;
  }
</style>
</head>
<body>
  <section class="card card--front">
    <div class="accent-bar"></div>
    <div class="wordmark">BRIGHTLEDGE</div>
    <div class="details">
      <h1 class="person-name"><span class="first">Colin</span> Merrow</h1>
      <p class="person-role">Financial Adviser</p>
      <p class="person-quals">BEc(Hons), AdDipFS(FP),<br>Dip FMBM, CFL®</p>
      <ul class="contact-list">
        <li>
          <svg viewBox="0 0 15 12" aria-hidden="true"><path fill="#006838" d="M1 3.5C3 1 12 1 14 3.5L14 5 11 5 10.5 3.8C9 3.3 6 3.3 4.5 3.8L4 5 1 5Z M3 6 L12 6 L13 11 L2 11Z"/><circle cx="7.5" cy="8.3" r="1.6" fill="#fff"/></svg>
          <span>0437 512 604</span>
        </li>
        <li>
          <svg viewBox="0 0 15 12" aria-hidden="true"><rect x="0.5" y="1" width="14" height="10" fill="#006838"/><path d="M1 1.5 7.5 7 14 1.5" fill="none" stroke="#fff" stroke-width="1.2"/></svg>
          <span>colin@brightledgeplan.com.au</span>
        </li>
      </ul>
    </div>
  </section>

  <section class="card card--back">
    <div class="wordmark">BRIGHTLEDGE</div>
    <div class="details">
      <ul class="company-info">
        <li>AFS Licence No. 518760</li>
        <li>www.brightledgeplan.com.au</li>
        <li>PO BOX 5307, PERTH BC, WA 6849</li>
      </ul>
    </div>
  </section>
</body>
</html>
```